HR services to some of biggest Silicon Valley Tech companies needs a new website

We need a new website design probably 4-5 pages initially. Here are some websites we like the look of https://quintarimhub.com/ , https://www.mervoly.com/ and https://tavrine.com/ .
Updates

Slow in providing feedback

Target Market(s)

Silicon valley tech companies

Industry/Entity Type

HR

Coding

Coded - Design and coding required

Number of Pages Required

5+ page

Requirements
Nice to have
• any stock photos or images should show a diverse group of people. Our client base is very diverse

```html
<!DOCTYPE html>
<html lang="en">
<head>
<meta charset="utf-8">
<title>HR Kestrel Consulting</title>
<link href="https://fonts.googleapis.com/css2?family=Montserrat:wght@400;500;600;700;800&display=swap" rel="stylesheet">
<style>
:root{
  --yellow:#ffc20e;
  --dark:#58585a;
  --darker:#4d4d4f;
  --text:#5b5b5d;
  --light:#f4f4f4;
  --white:#ffffff;
}
*{margin:0;padding:0;box-sizing:border-box}
html,body{width:1200px;height:4409px;overflow:hidden}
body{position:relative;font-family:'Montserrat',sans-serif;color:var(--text);background:var(--white)}
.abs{position:absolute}
.btn{position:absolute;display:flex;align-items:center;justify-content:center;background:var(--yellow);color:var(--dark);font-weight:700;font-size:15px;letter-spacing:.3px;text-transform:uppercase}
.btn.dark{background:var(--dark);color:var(--white)}
/* header */
.site-header{position:absolute;left:0;top:0;width:1200px;height:98px;background:var(--dark)}
.brand-tab{position:absolute;left:92px;top:0;width:222px;height:147px;background:var(--dark);clip-path:polygon(0 0,100% 0,100% 70%,88% 100%,12% 100%,0 70%)}
.brand{position:absolute;left:0;right:0;text-align:center;color:var(--white);font-weight:600;letter-spacing:1px}
.brand .dot{display:block;width:30px;height:30px;border-radius:50%;background:var(--yellow);margin:0 auto 10px}
.brand .name{font-size:23px;line-height:1}
.brand .name b{color:var(--yellow);font-weight:600}
.brand .sub{font-size:13px;letter-spacing:5px;margin-top:4px}
.main-nav{position:absolute;top:40px;left:0;font-size:15px;font-weight:700;color:var(--white)}
.main-nav span{position:absolute;white-space:nowrap}
.main-nav .active{color:var(--yellow)}
.phone-box{position:absolute;left:933px;top:0;width:267px;height:98px;background:var(--yellow);color:var(--dark);font-size:27px;font-weight:600;display:flex;align-items:center;justify-content:center}
/* hero */
.hero{position:absolute;left:0;top:98px;width:1200px;height:600px;background:linear-gradient(90deg,#eceeee 0%,#e2e4e4 45%,#b7a197 62%,#2a2a2e 72%,#d9dcdc 85%,#c9cccc 100%)}
.hero-title{position:absolute;left:108px;top:315px;font-size:44px;font-weight:700;color:var(--dark);letter-spacing:.5px}
.hero-title b{color:var(--yellow);font-weight:700}
.hero-sub{position:absolute;left:202px;top:376px;font-size:21px;font-weight:600;color:var(--dark)}
/* about */
.about{position:absolute;left:0;top:698px;width:1200px;height:528px;background:var(--dark)}
.about-mark{position:absolute;left:111px;top:81px;width:423px;height:364px;display:flex;flex-direction:column;align-items:center;justify-content:center;color:var(--white);font-weight:700}
.about-mark .circle{width:150px;height:150px;border-radius:50%;border:10px solid var(--yellow);margin-bottom:26px}
.about-mark .label{font-size:30px;letter-spacing:1px}
.about-title{position:absolute;left:621px;top:90px;font-size:50px;font-weight:700;color:var(--white)}
.about-title b{color:var(--yellow)}
.about-text{position:absolute;left:621px;top:163px;width:468px;font-size:13.4px;line-height:24.8px;color:var(--white);text-align:justify}
/* sections */
.section-title{position:absolute;left:0;width:1200px;text-align:center;font-size:36px;font-weight:700;color:var(--dark)}
.section-title b{color:var(--yellow)}
.services-intro{position:absolute;left:150px;top:1380px;width:900px;text-align:center;font-size:17px;line-height:28px}
.photo{position:absolute}
.service h3{position:absolute;font-size:32px;font-weight:700;color:var(--dark);line-height:34px}
.service ul{position:absolute;list-style:none;font-size:14.5px}
.service li{height:34px;display:flex;align-items:center}
.service li svg{margin-right:22px;flex:none}
.learn{position:absolute;font-size:15px;font-weight:700;color:var(--yellow)}
.badge{position:absolute;width:78px;height:78px;border-radius:50%;border:4px solid var(--white);box-shadow:0 0 0 1px #ddd;display:flex;align-items:center;justify-content:center}
/* team */
.team{position:absolute;left:0;top:2670px;width:1200px;height:570px;background:var(--light)}
.member-card{position:absolute;text-align:center;font-weight:700;font-size:15px;line-height:23px;padding-top:11px;background:var(--white);color:var(--dark);box-shadow:0 2px 6px rgba(0,0,0,.12)}
.member-card em{font-style:normal;color:var(--yellow);display:block}
.member-card.lead{background:var(--yellow)}
.member-card.lead em{color:var(--white)}
/* clients */
.client{position:absolute;top:3423px;width:183px;height:93px;background:var(--white);box-shadow:0 1px 6px rgba(0,0,0,.16);display:flex;align-items:center;justify-content:center;gap:8px;font-weight:700;font-size:17px;color:var(--dark)}
.client i{width:14px;height:14px;border-radius:50%;background:var(--yellow);display:block}
/* contact */
.contact{position:absolute;left:0;top:3611px;width:1200px;height:487px;background:var(--yellow)}
.contact-title{position:absolute;left:0;width:1200px;top:48px;text-align:center;font-size:35px;font-weight:700;color:var(--white)}
.contact-sub{position:absolute;left:0;width:1200px;top:100px;text-align:center;font-size:21px;font-weight:500;color:var(--white)}
.field{position:absolute;background:var(--white);font-size:14px;color:var(--dark);padding:15px 14px}
/* footer */
.site-footer{position:absolute;left:0;top:4098px;width:1200px;height:311px;background:var(--dark);color:var(--white)}
.foot-col{position:absolute;top:52px}
.foot-col h4{font-size:19px;font-weight:600;margin-bottom:20px}
.foot-col li{list-style:none;font-size:14px;height:25px;display:flex;align-items:center}
.foot-col li .chev{color:var(--yellow);width:34px;font-size:12px}
.foot-rule{position:absolute;left:111px;top:244px;width:978px;height:1px;background:#8a8a8c}
.copyright{position:absolute;left:111px;top:260px;font-size:13.5px}
.copyright b{font-weight:700}
.copyright b span{color:var(--yellow)}
.social{position:absolute;top:250px;width:36px;height:36px;border-radius:50%;border:2px solid var(--white);background:var(--yellow)}
</style>
</head>
<body>

<header class="site-header">
  <nav class="main-nav">
    <span class="active" style="left:352px">HOME</span>
    <span style="left:428px">ABOUT US</span>
    <span style="left:539px">SERVICES</span>
    <span style="left:645px">TEAM</span>
    <span style="left:717px">CLIENTS</span>
    <span style="left:811px">CONTACT</span>
  </nav>
  <div class="phone-box">123 - 456 - 7890</div>
</header>
<div class="brand-tab">
  <div class="brand" style="top:20px"><span class="dot"></span><div class="name">HR <b>KESTREL</b></div><div class="sub">CONSULTING</div></div>
</div>

<section class="hero" role="img" aria-label="Photo of a smiling businesswoman in a dark blazer standing in a bright office">
</section>
<h1 class="hero-title abs" style="top:315px">HR <b>KESTREL</b> CONSULTING</h1>
<p class="hero-sub">OUR TEAM SUPPORTS YOURS</p>
<a class="btn" style="left:293px;top:423px;width:154px;height:49px">Get Started</a>

<section class="about">
  <div class="about-mark"><span class="circle"></span><span class="label">HR KESTREL</span></div>
  <h2 class="about-title">ABOUT <b>US</b></h2>
  <p class="about-text">For fifteen years our team of industry experts has been providing HR consulting services with innovative strategies and a partnership mentality. We have worked with some of the most innovative companies in Silicon Valley, across a broad range of industries, and we're proud to grow our client list every year. HR Kestrel's experienced professionals help implement and maintain best practices, allowing our clients to focus on their core competencies</p>
  <a class="btn" style="left:621px;top:377px;width:146px;height:51px">Learn More</a>
</section>

<h2 class="section-title" style="top:1311px"><b>OUR</b> SERVICES</h2>
<p class="services-intro">We help assess your HR needs and offer ongoing HR Department services or defined projects based on your organization's unique needs and goals.</p>

<svg width="0" height="0" style="position:absolute">
  <defs>
    <symbol id="tick" viewBox="0 0 16 16"><circle cx="8" cy="8" r="7" fill="#ffc20e"/><path d="M4.5 8.2l2.3 2.3 4.7-4.8" stroke="#fff" stroke-width="1.8" fill="none"/></symbol>
  </defs>
</svg>

<div class="service">
  <div class="photo" style="left:599px;top:1494px;width:490px;height:360px;background:linear-gradient(135deg,#f2f3f3,#dcdfe0 55%,#c9c3bd)" role="img" aria-label="Photo of a woman with glasses working on a laptop in a bright office"></div>
  <h3 style="left:111px;top:1536px">SETUP</h3>
  <ul style="left:111px;top:1597px">
    <li><svg width="16" height="16"><use href="#tick"/></svg>Select and implement an HRIS system</li>
    <li><svg width="16" height="16"><use href="#tick"/></svg>Create Company Handbook</li>
    <li><svg width="16" height="16"><use href="#tick"/></svg>Write termination procedure</li>
    <li><svg width="16" height="16"><use href="#tick"/></svg>Set up benefits services</li>
    <li><svg width="16" height="16"><use href="#tick"/></svg>Set up workers comp vendor</li>
  </ul>
  <span class="learn" style="left:111px;top:1795px">LEARN MORE &nbsp;›</span>
  <div class="badge" style="left:560px;top:1637px;background:var(--dark)">
    <svg width="40" height="40" viewBox="0 0 40 40"><circle cx="20" cy="20" r="13" fill="none" stroke="#fff" stroke-width="3" stroke-dasharray="5 3"/><circle cx="20" cy="20" r="6" fill="none" stroke="#fff" stroke-width="2"/></svg>
  </div>
</div>

<div class="service">
  <div class="photo" style="left:111px;top:1854px;width:488px;height:361px;background:linear-gradient(135deg,#8a6a55,#3b3e44 50%,#d7dbe0)" role="img" aria-label="Photo of colleagues shaking hands across a meeting table"></div>
  <h3 style="left:685px;top:1898px">RECURRING PROCEDURES</h3>
  <ul style="left:685px;top:1957px">
    <li><svg width="16" height="16"><use href="#tick"/></svg>Review handbook annually</li>
    <li><svg width="16" height="16"><use href="#tick"/></svg>Roll out training (required and soft skills training)</li>
    <li><svg width="16" height="16"><use href="#tick"/></svg>Write offer letters</li>
    <li><svg width="16" height="16"><use href="#tick"/></svg>Handle employee data and files</li>
    <li><svg width="16" height="16"><use href="#tick"/></svg>Conduct I-9 audits</li>
  </ul>
  <span class="learn" style="left:685px;top:2156px">LEARN MORE &nbsp;›</span>
  <div class="badge" style="left:560px;top:1997px;background:var(--yellow)">
    <svg width="40" height="40" viewBox="0 0 40 40" fill="none" stroke="#fff" stroke-width="2.5"><circle cx="20" cy="12" r="5"/><circle cx="10" cy="17" r="3.5"/><circle cx="30" cy="17" r="3.5"/><path d="M11 32v-6a9 9 0 0118 0v6M3 30v-3a7 7 0 016-6M37 30v-3a7 7 0 00-6-6"/></svg>
  </div>
</div>

<div class="service">
  <div class="photo" style="left:599px;top:2215px;width:490px;height:359px;background:linear-gradient(135deg,#a98d78,#6e6560 45%,#2f3136 70%,#c6c1bb)" role="img" aria-label="Photo of a woman listening to a colleague during a meeting"></div>
  <h3 style="left:111px;top:2259px">PARTNER COMMUNICATIONS<br>AND PROJECTS</h3>
  <ul style="left:111px;top:2350px">
    <li><svg width="16" height="16"><use href="#tick"/></svg>Manage annual bidding process for benefits review</li>
    <li><svg width="16" height="16"><use href="#tick"/></svg>Handle EDD inquires</li>
    <li><svg width="16" height="16"><use href="#tick"/></svg>Partner on M&amp;A activity</li>
    <li><svg width="16" height="16"><use href="#tick"/></svg>Handle workers compensation claims administration</li>
  </ul>
  <span class="learn" style="left:111px;top:2516px">LEARN MORE &nbsp;›</span>
  <div class="badge" style="left:560px;top:2357px;background:var(--dark)">
    <svg width="40" height="40" viewBox="0 0 40 40" fill="none" stroke="#fff" stroke-width="2.5"><circle cx="12" cy="25" r="6"/><circle cx="28" cy="25" r="6"/><path d="M14 8h14v8l-4-3"/></svg>
  </div>
</div>

<section class="team">
  <h2 class="section-title" style="top:50px"><b>OUR</b> TEAM</h2>
  <div class="photo" style="left:111px;top:142px;width:231px;height:235px;background:linear-gradient(160deg,#6f8a9c,#c9ccc9 60%,#8f8f8f)" role="img" aria-label="Portrait of the company CEO"></div>
  <div class="photo" style="left:359px;top:142px;width:232px;height:235px;background:linear-gradient(160deg,#eaeaea,#8a8a8a 60%,#4a4a4a)" role="img" aria-label="Black and white portrait of a staff member"></div>
  <div class="photo" style="left:608px;top:142px;width:232px;height:235px;background:linear-gradient(160deg,#9a9a9a,#5a5a5a 55%,#bdbdbd)" role="img" aria-label="Black and white portrait of a staff member"></div>
  <div class="photo" style="left:856px;top:142px;width:233px;height:235px;background:linear-gradient(160deg,#d6d6d6,#6a6a6a 55%,#e6e6e6)" role="img" aria-label="Black and white portrait of a staff member"></div>
  <div class="member-card lead" style="left:134px;top:342px;width:188px;height:65px">MARA ELLISON<em>CEO</em></div>
  <div class="member-card" style="left:381px;top:342px;width:188px;height:65px">JONAH PIERCE<em>STAFF</em></div>
  <div class="member-card" style="left:630px;top:342px;width:188px;height:65px">LENA ORTIZ<em>STAFF</em></div>
  <div class="member-card" style="left:878px;top:342px;width:188px;height:65px">PRIYA NANDI<em>STAFF</em></div>
  <a class="btn" style="left:514px;top:459px;width:171px;height:50px">Meet Our Team</a>
</section>

<h2 class="section-title" style="top:3329px"><b>OUR</b> CLIENTS</h2>
<svg class="abs" style="left:50px;top:3456px" width="20" height="28" viewBox="0 0 20 28"><path d="M15 3L5 14l10 11" stroke="#c9c9c9" stroke-width="3" fill="none"/></svg>
<svg class="abs" style="left:1131px;top:3456px" width="20" height="28" viewBox="0 0 20 28"><path d="M5 3l10 11L5 25" stroke="#ffc20e" stroke-width="3" fill="none"/></svg>
<div class="client" style="left:110px"><i></i>CONSULT</div>
<div class="client" style="left:308px"><i></i>COMPANY NAME</div>
<div class="client" style="left:508px"><i></i>CONSULT</div>
<div class="client" style="left:707px"><i></i>HR COMPANY</div>
<div class="client" style="left:905px"><i></i>BrandName</div>

<section class="contact">
  <h2 class="contact-title">CONACT US</h2>
  <p class="contact-sub">We look forward to working with you</p>
  <div class="field" style="left:217px;top:161px;width:377px;height:47px">First Name</div>
  <div class="field" style="left:604px;top:161px;width:378px;height:47px">Last Name</div>
  <div class="field" style="left:217px;top:218px;width:377px;height:46px">Phone Number</div>
  <div class="field" style="left:604px;top:218px;width:378px;height:46px">Email Address</div>
  <div class="field" style="left:217px;top:274px;width:765px;height:96px">Enter Your Message</div>
  <a class="btn dark" style="left:484px;top:389px;width:231px;height:50px">Free Consultation</a>
</section>

<footer class="site-footer">
  <div class="brand" style="left:111px;right:auto;width:194px;top:40px"><span class="dot" style="width:44px;height:44px"></span><div class="name" style="font-size:30px">HR <b>KESTREL</b></div><div class="sub" style="font-size:16px;letter-spacing:6px">CONSULTING</div></div>
  <div class="foot-col" style="left:400px"><h4>Quick Links</h4><ul>
    <li><span class="chev">»</span>Home</li><li><span class="chev">»</span>About Us</li><li><span class="chev">»</span>Services</li><li><span class="chev">»</span>Our Team</li><li><span class="chev">»</span>Clients</li></ul></div>
  <div class="foot-col" style="left:613px"><h4>Other Links</h4><ul>
    <li><span class="chev">»</span>Privacy Policy</li><li><span class="chev">»</span>Terms Of Use</li><li><span class="chev">»</span>Legal Support</li></ul></div>
  <div class="foot-col" style="left:844px"><h4>Contact Us</h4><ul>
    <li style="height:50px;align-items:flex-start"><span class="chev"><svg width="12" height="15" viewBox="0 0 12 15"><path d="M6 14s5-5 5-8.5A5 5 0 001 5.5C1 9 6 14 6 14z" fill="#ffc20e"/><circle cx="6" cy="5.5" r="2" fill="#58585a"/></svg></span>465, Lorum Ipsum Dol,<br>United States</li>
    <li><span class="chev"><svg width="13" height="13" viewBox="0 0 13 13"><path d="M2 1l3 3-1.5 2a7 7 0 003.5 3.5L9 8l3 3-2 2C5 13 0 8 0 3z" fill="#ffc20e"/></svg></span>123 - 456 - 7890</li>
    <li><span class="chev"><svg width="14" height="11" viewBox="0 0 14 11"><rect x="1" y="1" width="12" height="9" fill="none" stroke="#ffc20e" stroke-width="1.5"/><path d="M1 1l6 5 6-5" fill="none" stroke="#ffc20e" stroke-width="1.5"/></svg></span>info@kestrelhrgroup.com</li></ul></div>
  <div class="foot-rule"></div>
  <p class="copyright">© 2021 <b>HR <span>KESTREL</span> CONSULTING</b>. All Rights Reserved</p>
  <span class="social" style="left:923px"></span>
  <span class="social" style="left:966px"></span>
  <span class="social" style="left:1009px"></span>
  <span class="social" style="left:1052px"></span>
</footer>

</body>
</html>
```